Web page update/ Create new non flash site

I have a flash web page, created by my ex girlfriend through some kind of web design service. I want to take all of the information that I have on the page and put it together in a similar manner on a non-flash page.I want to add a lot of pictures, update the logo to the one i had made on pixel forge and reword a few things to reflect the the direction my business has gone in, in the past couple years since I made the site.. I also can't figure out why when people e-mail me from my page, I get the e-mail but no message, happens all the time and makes me think I'm losing business. My main problem is that I don't know what service was used in the past to create this page or what information someone would need to be able to work on it more. I also have another domain name that I want connected to it. the existing web page is at www.ferrowbuilders.example

Target Market(s)

I originally made this web page thinking that i was going to be in the remodeling business, but the majority of the work i get is for high end commercial and residential millwork and carpentry installations. I mainly will be advertising to other general contractors, but I want to keep the same feel that it has now, how it is mainly talking to homeowners that are thinking about hiring me to do some sort of project for them.

Industry/Entity Type

Business

Requirements
Must have
• Portfolio page needs to be updated to have LOTS more pictures and have them in an organized manner where it's easy to navigate through them. My other main thing is that I want to keep the same look and feel that it has with the nice woodgrain background, user friendly layout of links, etc.

```html
<!DOCTYPE html>
<html lang="en">
<head>
<meta charset="utf-8">
<title>Ferrow Builders – building &amp; renovation company</title>
<link rel="stylesheet" href="https://fonts.googleapis.com/css2?family=Didact+Gothic&family=PT+Sans+Narrow&family=PT+Sans:wght@400&display=swap">
<style>
:root{
  --page:#e8e8e8;
  --topbar:#1b1b1b;
  --blue:#0ea3d6;
  --blue-light:#2ab8e6;
  --band:#1a1a1a;
  --footer:#262626;
  --white:#ffffff;
  --ink:#1d1d1d;
  --body-text:#5a5a5a;
  --footer-text:#b8b8b8;
  --dot-active:#3a6fd0;
  --dot:#2a2a2a;
  --green:#39b54a;
  --green-dark:#2a8a38;
}
*{margin:0;padding:0;box-sizing:border-box}
html,body{width:898px;height:1200px;overflow:hidden}
body{position:relative;background:var(--page);font-family:"PT Sans",sans-serif;color:var(--ink)}
h1,h2,h3{font-weight:400}
.abs{position:absolute}
.topbar{left:0;top:0;width:898px;height:42px;background:var(--topbar)}
.ribbon{left:67px;top:12px;width:766px;height:60px;background:var(--blue);clip-path:polygon(0 0,100% 0,98.8% 100%,1.2% 100%)}
.ribbon-shadow{left:67px;top:70px;width:766px;height:6px;background:linear-gradient(rgba(0,0,0,.12),rgba(0,0,0,0))}
.logo{left:95px;top:3px;width:234px;height:60px;background:linear-gradient(var(--blue-light),var(--blue));box-shadow:0 2px 4px rgba(0,0,0,.25);text-align:right;padding:13px 14px 0 0;font-family:"Didact Gothic",sans-serif;color:var(--white)}
.logo .name{font-size:22px;line-height:22px}
.logo .tag{font-size:11.5px;line-height:14px}
.nav{left:346px;top:32px;display:flex;align-items:center;font-family:"PT Sans Narrow",sans-serif;font-size:14px;color:var(--white);text-transform:uppercase}
.nav a{color:inherit;text-decoration:none;padding:0 17px;border-left:1px solid rgba(255,255,255,.35);line-height:16px}
.nav a:first-child{border-left:0}
.slider{left:96px;top:97px;width:713px;height:339px;background:var(--white);padding:6px}
.slider .photo{width:100%;height:100%;background:linear-gradient(160deg,#4a6a90 0%,#8fb6d6 35%,#2f7fc9 60%,#1a3f9a 100%)}
.dots{left:432px;top:449px;display:flex;gap:5px}
.dots span{width:10px;height:10px;border-radius:50%;background:var(--dot)}
.dots span.on{background:var(--dot-active)}
.gallery{left:0;top:492px;width:898px;height:165px;background:var(--band)}
.section-title{font-family:"PT Sans Narrow",sans-serif;font-weight:400;font-size:21px;text-transform:uppercase;line-height:22px}
.gallery .section-title{left:64px;top:19px;color:var(--white)}
.thumb{top:53px;width:110px;height:96px;background:var(--white);padding:5px}
.thumb div{width:100%;height:100%}
.arrow{top:90px;width:22px;height:22px;background:var(--blue)}
.card{top:681px;height:271px;background:var(--white);border-radius:4px}
.card .section-title{position:absolute;left:19px;top:22px;font-size:21px}
.card p{position:absolute;left:19px;width:350px;font-size:9.4px;line-height:13.5px;color:var(--body-text);text-align:justify}
.card .icon{position:absolute;top:12px;width:36px;height:34px}
.footer{left:0;top:978px;width:898px;height:222px;background:var(--footer)}
.links{top:28px}
.links h3{font-family:"PT Sans Narrow",sans-serif;font-size:18px;color:var(--white);text-transform:uppercase;margin-bottom:9px;line-height:20px}
.links ul{list-style:none}
.links li{font-size:9px;line-height:22.4px;color:var(--white);position:relative;padding-left:15px}
.links li::before{content:"";position:absolute;left:0;top:9px;width:4px;height:2px;border-left:1.5px solid var(--blue);border-bottom:1.5px solid var(--blue);transform:rotate(-45deg)}
.foot-brand{right:64px;top:28px;text-align:right;font-family:"Didact Gothic",sans-serif;color:var(--white)}
.foot-brand .name{font-size:22px;line-height:24px}
.foot-brand .tag{font-size:11.5px;line-height:14px}
.foot-about{left:601px;top:75px;width:233px;font-size:9px;line-height:13.6px;color:var(--footer-text);text-align:justify}
.copyright{right:64px;top:170px;font-size:9px;color:var(--white)}
</style>
</head>
<body>
<header>
  <div class="abs topbar"></div>
  <div class="abs ribbon"></div>
  <div class="abs ribbon-shadow"></div>
  <div class="abs logo"><div class="name">Ferrow Builders</div><div class="tag">building &amp; renovation company</div></div>
  <nav class="abs nav"><a href="#">Home</a><a href="#">About Us</a><a href="#">Services</a><a href="#">Portfolio</a><a href="#">Process</a><a href="#">Contact Us</a></nav>
</header>

<section class="abs slider"><div class="photo" role="img" aria-label="Featured project photo: glass and steel atrium roof against a blue sky"></div></section>
<div class="abs dots"><span class="on"></span><span></span><span></span></div>

<section class="abs gallery">
  <h2 class="abs section-title">Photo Gallery</h2>
  <div class="abs arrow" style="left:64px"><svg width="22" height="22" viewBox="0 0 22 22"><path d="M7 11h8M7 11l3-3M7 11l3 3" stroke="#fff" stroke-width="1.6" fill="none"/></svg></div>
  <div class="abs thumb" style="left:95px"><div role="img" aria-label="Tiled bathroom wall with window" style="background:linear-gradient(90deg,#6b5a50,#8a776b)"></div></div>
  <div class="abs thumb" style="left:215px"><div role="img" aria-label="Ceiling trim and millwork detail" style="background:linear-gradient(160deg,#e0d8cc,#9a7a55)"></div></div>
  <div class="abs thumb" style="left:334px"><div role="img" aria-label="Hallway with pendant light and doorway" style="background:linear-gradient(90deg,#3a2e26,#6b5a48)"></div></div>
  <div class="abs thumb" style="left:454px"><div role="img" aria-label="Tiled bathroom wall with window" style="background:linear-gradient(90deg,#6b5a50,#8a776b)"></div></div>
  <div class="abs thumb" style="left:573px"><div role="img" aria-label="Hallway with pendant light and doorway" style="background:linear-gradient(90deg,#3a2e26,#6b5a48)"></div></div>
  <div class="abs thumb" style="left:693px"><div role="img" aria-label="Kitchen with dark wood cabinetry" style="background:linear-gradient(160deg,#4a2c1c,#7a4a2a)"></div></div>
  <div class="abs arrow" style="left:813px"><svg width="22" height="22" viewBox="0 0 22 22"><path d="M7 11h8M15 11l-3-3M15 11l-3 3" stroke="#fff" stroke-width="1.6" fill="none"/></svg></div>
</section>

<main>
  <article class="abs card" style="left:65px;width:375px">
    <h2 class="section-title">Welcome</h2>
    <svg class="icon" style="left:318px" viewBox="0 0 36 34" aria-hidden="true"><path d="M18 2L2 17h5v15h22V17h5z" fill="var(--green)"/><rect x="15" y="22" width="6" height="10" fill="var(--green-dark)"/></svg>
    <p style="top:58px">Lorem Ipsum is simply dummy text of the printing and typesetting industry. Lorem Ipsum has been the industry's standard dummy text ever since the 1500s, when an unknown printer took a galley of type and scrambled it to make a type specimen book. It has survived not only five centuries, but also the leap into electronic type-setting, remaining essentially unchanged. It was popularised in the 1960s with the release of Lettrex sheets containing Lorem Ipsum passages, and more recently with desktop publishing software like Quill PageSetter including versions of Lorem Ipsum.</p>
    <p style="top:179px">It has survived not only five centuries, but also the leap into electronic typesetting, remaining essentially unchanged. It was popularised in the 1960s with the release of Lettrex sheets containing Lorem Ipsum passages, and more recently with desk-top publishing software like Quill PageSetter including versions of Lorem Ipsum.</p>
  </article>
  <article class="abs card" style="left:466px;width:370px">
    <h2 class="section-title">Why Choose Ferrow Builders?</h2>
    <div class="icon" style="left:318px;border-radius:6px;background:linear-gradient(90deg,#7ac04a,#8aa4c8,#f08a30)" role="img" aria-label="Team icon"></div>
    <p style="top:58px;left:28px;width:335px">Lorem Ipsum is simply dummy text of the printing and typesetting industry. Lorem Ipsum has been the industry's standard dummy text ever since the 1500s, when an unknown printer took a galley of type and scrambled it to make a type specimen book. It has survived not only five centuries, but also the leap into electronic type-setting, remaining essentially unchanged. It was popularised in the 1960s with the release of Lettrex sheets containing Lorem Ipsum passages, and more recently with desktop publishing software like Quill PageSetter including versions of Lorem Ipsum.</p>
    <p style="top:179px;left:28px;width:335px">It has survived not only five centuries, but also the leap into electronic typesetting, remaining essentially unchanged. It was popularised in the 1960s with the release of Lettrex sheets containing Lorem Ipsum passages, and more recently with desk-top publishing software like Quill PageSetter including versions of Lorem Ipsum.</p>
  </article>
</main>

<footer class="abs footer">
  <div class="abs links" style="left:65px"><h3>Quick Links</h3><ul><li>Lorem Ipsum</li><li>Lorem Ipsum</li><li>Lorem Ipsum</li><li>Lorem Ipsum</li><li>Lorem Ipsum</li><li>Lorem Ipsum</li><li>Lorem Ipsum</li></ul></div>
  <div class="abs links" style="left:193px"><h3>Quick Links</h3><ul><li>Lorem Ipsum</li><li>Lorem Ipsum</li><li>Lorem Ipsum</li><li>Lorem Ipsum</li><li>Lorem Ipsum</li><li>Lorem Ipsum</li><li>Lorem Ipsum</li></ul></div>
  <div class="abs links" style="left:327px"><h3>Quick Links</h3><ul><li>Lorem Ipsum</li><li>Lorem Ipsum</li><li>Lorem Ipsum</li><li>Lorem Ipsum</li><li>Lorem Ipsum</li><li>Lorem Ipsum</li><li>Lorem Ipsum</li></ul></div>
  <div class="abs links" style="left:485px"><h3>Quick Links</h3><ul><li>Lorem Ipsum</li><li>Lorem Ipsum</li><li>Lorem Ipsum</li><li>Lorem Ipsum</li><li>Lorem Ipsum</li><li>Lorem Ipsum</li><li>Lorem Ipsum</li></ul></div>
  <div class="abs foot-brand"><div class="name">Ferrow Builders</div><div class="tag">building &amp; renovation company</div></div>
  <p class="abs foot-about">Lorem Ipsum is simply dummy text of the printing and typesing industry. Lorem Ipsum has been the industry's standard dummy text ever since the 1500s, when an unknown printer took a galley of type and scrambled it to make a type specimen book. It has survived not only five centuries...</p>
  <p class="abs copyright">© 2012. All Rights Reserved.</p>
</footer>
</body>
</html>
```